Website for UK Fintech Company specialising in Auto-Finance asset management

We need a website for a FINTECH business called KELP Asset Management. We have developed and licenced an innovative platform to provide financial institutions whom provide secured Asset finance loans to consumer and commercial clients, allowing for real time tracking and management of defaulted accounts pending repossession. The KELP Asset Management platform is a total recoveries solution through the cycle, from the moment the lender has to recover the vehicle (due to default/non-payment) to the disposal of the vehicle (via sale at Motor Auctions or by selling to a Car dealership network). The data provided from external services allows the Financier to make informed decisions, such as whether it is economical to continue the recovery and decide which sales channel is better suited for their assets to maximise residual values and minimise financial losses. The KELP platform provides an array of MI reporting and uses a systematic approach utilising exception reporting to identify key areas of non-performance to enable focus where needed. KELP also provides a leading Debt collection service recovering end-of-cycle losses such as Financial Shortfall and losses in vehicle values due to conditions and excessive damage.

We also require a new logo for out new product called MB-Prismo

Target Market(s)

Financial institutions whom provide secured Asset finance loans to consumer and commercial clients

Industry/Entity Type

Financial Service

Logo Text

MB- Prismo (this is for a new product which forms part of the KELP Asset Mangement Platform

Number of Pages Required

4 page

Font styles to use
Serif
Sans Serif

Colors

Designer to choose colors to be used in the design.

Requirements
Must have
• We need a simple website with a broken down as follows;
• • Landing page
• • Services page
• • About us page
• • KELP Asset Management Platform login page (client facing)
Nice to have
• Our slogan is 'Auto-Finance Expertise'
• We are very much open to suggestions as long as we can create a professional/ corporate / modern feel to the website. We are a FINTECH company, and that needs to come across
Should not have
• Whilst we are an asset management company primarily managing vehicles through our platform, we don't want it to look like a car dealership website!:)

```html
<!DOCTYPE html>
<html lang="en">
<head>
<meta charset="utf-8">
<title>KELP Asset Management – About Us</title>
<link href="https://fonts.googleapis.com/css2?family=Open+Sans:wght@300;400;600;700;800&display=swap" rel="stylesheet">
<style>
  :root {
    --orange: #ef7d00;
    --orange-soft: rgba(239, 125, 0, 0.78);
    --orange-pale: rgba(247, 190, 130, 0.55);
    --ink: #3a3a3a;
    --text: #555555;
    --muted: #666666;
    --white: #ffffff;
    --page: #ffffff;
  }
  * { margin: 0; padding: 0; box-sizing: border-box; }
  html, body { width: 768px; height: 1200px; overflow: hidden; background: var(--page); }
  body { position: relative; font-family: "Open Sans", Arial, sans-serif; color: var(--text); }
  .abs { position: absolute; }

  .top-rule { left: 0; top: 0; width: 768px; height: 3px; background: var(--orange); }

  .brand { left: 64px; top: 22px; }
  .brand-name { font-size: 36px; font-weight: 700; color: var(--ink); letter-spacing: -1px; line-height: 1; }

  .contact-email { left: 476px; top: 14px; font-size: 12px; color: var(--muted); display: flex; align-items: center; gap: 3px; }
  .call-btn { left: 647px; top: 14px; width: 57px; height: 16px; background: var(--orange); color: var(--white); font-size: 8px; font-weight: 600; text-align: center; line-height: 16px; }

  .nav a { position: absolute; top: 45px; font-size: 12px; color: var(--ink); text-decoration: none; }
  .nav-underline { left: 479px; top: 64px; width: 51px; height: 3px; background: var(--orange); }

  .hero { left: 0; top: 89px; width: 768px; height: 267px; background: linear-gradient(120deg, #8a8e92 0%, #d9dde0 35%, #eef0f2 60%, #c9b7a6 85%, #e9e9ea 100%); }
  .hero-title-band { left: 0; top: 170px; width: 326px; height: 30px; background: var(--orange-soft); }
  .hero-title { left: 65px; top: 174px; font-size: 18px; color: var(--white); font-weight: 400; }
  .hero-text-band { left: 0; top: 222px; width: 420px; height: 50px; background: var(--orange-pale); }
  .hero-text { left: 65px; top: 236px; width: 350px; font-size: 9.6px; line-height: 11.5px; color: var(--white); }

  .section-title { font-size: 24px; font-weight: 300; color: var(--text); }
  .about-title { left: 0; width: 768px; top: 390px; text-align: center; }
  .about-text { left: 65px; top: 450px; width: 640px; font-size: 11.3px; line-height: 17.6px; }

  .slogan { left: 66px; top: 519px; font-size: 33.5px; font-weight: 800; line-height: 41.6px; color: var(--ink); }
  .slogan .accent { color: var(--orange); }

  .who-title { left: 331px; top: 518px; }
  .who-text { left: 257px; top: 558px; width: 445px; font-size: 11.3px; line-height: 17.6px; }
  .expertise-text { left: 66px; top: 643px; width: 432px; font-size: 11.3px; line-height: 17.6px; }

  .tech-photo { left: 502px; top: 648px; width: 200px; height: 130px; border: 3px solid var(--orange); background: linear-gradient(135deg, #0d3a78 0%, #2f6fb8 45%, #b9d3ee 65%, #1c4e92 100%); }

  .team-title { left: 0; width: 768px; top: 819px; text-align: center; }
  .team-photo { top: 872px; width: 88px; height: 87px; border: 2px solid var(--orange); border-radius: 7px; background: linear-gradient(160deg, #eceef0 0%, #c9ccd0 50%, #2a2a2e 100%); }

  .team-card { left: 64px; top: 978px; width: 382px; height: 137px; background: var(--orange); border-radius: 6px; }
  .team-card-pointer { left: 189px; top: 958px; }
  .team-icon { left: 74px; top: 1029px; }
  .team-card-title { left: 125px; top: 983px; font-size: 14.4px; font-weight: 400; color: var(--white); }
  .team-card-text { left: 126px; top: 1005px; width: 310px; font-size: 9.4px; line-height: 11.4px; color: var(--white); }

  .role-bubble { left: 479px; top: 871px; width: 225px; height: 30px; background: var(--orange); border-radius: 6px; color: var(--white); font-size: 15.5px; font-weight: 700; text-align: center; line-height: 30px; }
  .role-pointer { left: 664px; top: 900px; }
  .role-text { left: 481px; top: 917px; width: 220px; font-size: 9px; line-height: 11.5px; }

  .point-check { left: 483px; }
  .point-title { left: 528px; font-size: 15px; font-weight: 700; color: var(--orange); }
  .point-text { left: 529px; width: 156px; font-size: 8.8px; line-height: 11px; }

  .footer-brand { left: 93px; top: 1161px; }
  .footer-brand .brand-name { font-size: 19px; letter-spacing: -0.5px; }
  .copyright { left: 0; width: 762px; top: 1170px; text-align: center; font-size: 9.6px; color: var(--text); }
  .social { left: 567px; top: 1168px; display: flex; gap: 7.5px; }
  .social span { width: 15px; height: 15px; border: 1.3px solid var(--orange); border-radius: 50%; display: block; }
</style>
</head>
<body>
  <div class="abs top-rule"></div>

  <header>
    <div class="abs brand"><span class="brand-name">KELP</span></div>
    <div class="abs contact-email">
      <svg width="16" height="16" viewBox="0 0 16 16" aria-hidden="true"><circle cx="8" cy="8" r="7" fill="none" stroke="#ef7d00" stroke-width="1.3"/><rect x="4" y="5.2" width="8" height="5.6" fill="none" stroke="#ef7d00" stroke-width="1"/><path d="M4 5.2 L8 8.4 L12 5.2" fill="none" stroke="#ef7d00" stroke-width="1"/></svg>
      hello@kelpassets.co.uk
    </div>
    <div class="abs call-btn">Call Us</div>
    <nav class="nav">
      <a style="left:394px">Home</a>
      <a style="left:480px">About Us</a>
      <a style="left:566px">Services</a>
      <a style="left:652px">Login
        <svg width="10" height="11" viewBox="0 0 10 11" aria-hidden="true"><circle cx="5" cy="3" r="2.6" fill="#222"/><path d="M0.5 11 C0.5 6.5 9.5 6.5 9.5 11 Z" fill="#222"/></svg>
      </a>
    </nav>
    <div class="abs nav-underline"></div>
  </header>

  <section>
    <div class="abs hero" role="img" aria-label="Business people signing finance documents at a desk"></div>
    <div class="abs hero-title-band"></div>
    <h1 class="abs hero-title">WELCOME TO KELP</h1>
    <div class="abs hero-text-band"></div>
    <p class="abs hero-text">Lorem ipsum dolor sit amet, amet feugiat lacus, pretium imperdiet, consectetuer rutrum dui et, quam vitae accumsan eleifend mattis adipiscing duis.</p>
  </section>

  <section>
    <h2 class="abs section-title about-title">About Us</h2>
    <p class="abs about-text">We have developed and licenced an innovative platform to provide financial institutions whom provide secured Asset finance loans to consumer and commercial clients, allowing for real time tracking and management of defaulted accounts pending repossession.</p>

    <div class="abs slogan">AUTO<br>FINANCE<br><span class="accent">EXPERTISE</span></div>

    <h2 class="abs section-title who-title">Who We Are</h2>
    <p class="abs who-text">Lorem ipsum dolor sit amet, amet feugiat lacus, pretium imperdiet, consectetuer rutrum dui et, quam vitae accumsan eleifend mattis adipiscing duis. Scelerisque dapibus gravida nam, semper leo neque cras habitasse suspendisse dignissim, massa vehicula facilisis, ut et. Pellentesque vestibulum. Amet metus volutpat mauris</p>

    <p class="abs expertise-text">Lorem ipsum dolor sit amet, amet feugiat lacus, pretium imperdiet, consectetuer rutrum dui et, quam vitae accumsan eleifend mattis adipiscing duis. Scelerisque dapibus gravida nam, semper leo neque cras habitasse suspendisse dignissim, massa vehicula facilisis, ut et. Pellentesque vestibulum. Amet metus volutpat mauris in. Nulla duis pede morbi, curabitur purus nec ut, massa vel ridiculus eu eget, rutrum sem feugiat facilisis, mauris diam purus fringilla purus sed. Felis mollis ultricies enim.</p>

    <div class="abs tech-photo" role="img" aria-label="Hand on a laptop with glowing blue financial data graphics"></div>
  </section>

  <section>
    <h2 class="abs section-title team-title">Meet Our Team</h2>
    <div class="abs team-photo" style="left:64px" role="img" aria-label="Two colleagues in business suits holding a laptop"></div>
    <div class="abs team-photo" style="left:162px" role="img" aria-label="Two colleagues in business suits holding a laptop"></div>
    <div class="abs team-photo" style="left:259px" role="img" aria-label="Two colleagues in business suits holding a laptop"></div>
    <div class="abs team-photo" style="left:356px" role="img" aria-label="Two colleagues in business suits holding a laptop"></div>

    <svg class="abs team-card-pointer" width="41" height="22" viewBox="0 0 41 22" aria-hidden="true"><path d="M0 22 L13 0 L28 0 L41 22 Z" fill="#ef7d00"/></svg>
    <div class="abs team-card"></div>
    <svg class="abs team-icon" width="48" height="32" viewBox="0 0 48 32" aria-hidden="true" fill="#ffffff">
      <circle cx="10" cy="8" r="5"/><path d="M0 30 C0 17 20 17 20 30 Z"/>
      <circle cx="38" cy="8" r="5"/><path d="M28 30 C28 17 48 17 48 30 Z"/>
      <circle cx="24" cy="7" r="6"/><path d="M12 32 C12 16 36 16 36 32 Z"/>
    </svg>
    <h3 class="abs team-card-title">Title</h3>
    <p class="abs team-card-text">Lorem ipsum dolor sit amet, amet feugiat lacus, pretium imperdiet, consectetuer rutrum dui et, quam vitae accumsan eleifend mattis adipiscing duis. Scelerisque dapibus gravida nam, semper leo neque cras habitasse suspendisse dignissim, massa vehicula facilisis, ut et. Pellentesque vestibulum. Amet metus volutpat mauris in. Nulla duis pede morbi, curabitur purus nec ut, massa vel ridiculus eu eget, rutrum sem feugiat facilisis, mauris diam purus fringilla purus sed. Felis mollis ultricies enim.</p>

    <div class="abs role-bubble">Management Consultant</div>
    <svg class="abs role-pointer" width="14" height="20" viewBox="0 0 14 20" aria-hidden="true"><path d="M0 0 L14 0 L8 20 Z" fill="#ef7d00"/></svg>
    <p class="abs role-text">Lorem ipsum dolor sit amet, amet feugiat lacus, pretium imperdiet, consectetuer rutrum dui et, quam vitae accumsan eleifend mattis adipiscing duis.</p>

    <svg class="abs point-check" style="top:984px" width="31" height="31" viewBox="0 0 31 31" aria-hidden="true"><circle cx="15.5" cy="15.5" r="15.5" fill="#ef7d00"/><path d="M8.5 16 L13.5 21 L23 10.5" fill="none" stroke="#fff" stroke-width="3.2" stroke-linecap="round" stroke-linejoin="round"/></svg>
    <h4 class="abs point-title" style="top:967px">Number One</h4>
    <p class="abs point-text" style="top:990px">Lorem ipsum dolor sit amet, amet feugiat lacus, pretium imperdiet.</p>

    <svg class="abs point-check" style="top:1036px" width="31" height="31" viewBox="0 0 31 31" aria-hidden="true"><circle cx="15.5" cy="15.5" r="15.5" fill="#ef7d00"/><path d="M8.5 16 L13.5 21 L23 10.5" fill="none" stroke="#fff" stroke-width="3.2" stroke-linecap="round" stroke-linejoin="round"/></svg>
    <h4 class="abs point-title" style="top:1019px">Number Two</h4>
    <p class="abs point-text" style="top:1042px">Lorem ipsum dolor sit amet, amet feugiat lacus, pretium imperdiet.</p>

    <svg class="abs point-check" style="top:1087px" width="31" height="31" viewBox="0 0 31 31" aria-hidden="true"><circle cx="15.5" cy="15.5" r="15.5" fill="#ef7d00"/><path d="M8.5 16 L13.5 21 L23 10.5" fill="none" stroke="#fff" stroke-width="3.2" stroke-linecap="round" stroke-linejoin="round"/></svg>
    <h4 class="abs point-title" style="top:1070px">Number Three</h4>
    <p class="abs point-text" style="top:1093px">Lorem ipsum dolor sit amet, amet feugiat lacus, pretium imperdiet.</p>
  </section>

  <footer>
    <div class="abs footer-brand"><span class="brand-name">KELP</span></div>
    <p class="abs copyright">Copyright © 2018. All Rights Reserved</p>
    <div class="abs social" aria-label="Social links"><span></span><span></span><span></span><span></span><span></span></div>
  </footer>
</body>
</html>
```